Business Card Design

Harbourline Recruitment is a specialist financial services recruitment company and implementation partner

Industry/Entity Type

Business

Contact Information for Business Card

Tom Ashford
Harbourline Recruitment Ltd
e:tom.ashford@harbourline-staffing.com
m:07834 206 148
m:07712 438 560
s: tommashford

```html
<!DOCTYPE html>
<html lang="en">
<head>
<meta charset="utf-8">
<title>Harbourline Recruitment – Business Card</title>
<link rel="stylesheet" href="https://fonts.googleapis.com/css2?family=Mulish:wght@600;700&family=Open+Sans:wght@400;600&display=swap">
<style>
  :root {
    --stage: #ecebe9;
    --card: #ffffff;
    --accent: #d9480f;
    --ink: #3a3a3a;
    --on-accent: #ffffff;
    --shadow: rgba(0, 0, 0, 0.18);
  }
  * { box-sizing: border-box; margin: 0; padding: 0; }
  html, body {
    width: 1200px;
    height: 900px;
    overflow: hidden;
    background: var(--stage);
  }
  .stage { position: relative; width: 1200px; height: 900px; }

  .card {
    position: absolute;
    width: 587px;
    height: 362px;
    background: var(--card);
    border-radius: 14px;
    overflow: hidden;
    box-shadow: 0 6px 18px var(--shadow);
  }
  .card--front { left: 78px; top: 35px; }
  .card--back  { left: 380px; top: 500px; }

  .front-band { position: absolute; inset: 0; }

  .front-title {
    position: absolute;
    left: 222px;
    top: 150px;
    transform: translate(-50%, -50%) rotate(-31deg);
    font-family: "Mulish", sans-serif;
    font-weight: 700;
    font-size: 27px;
    color: var(--ink);
    white-space: nowrap;
  }

  .contact {
    position: absolute;
    right: 36px;
    top: 193px;
    text-align: right;
    font-family: "Open Sans", sans-serif;
    color: var(--on-accent);
  }
  .contact__name {
    font-weight: 600;
    font-size: 21px;
    margin-bottom: 12px;
  }
  .contact__line {
    display: flex;
    justify-content: flex-end;
    align-items: center;
    gap: 10px;
    font-size: 15px;
    height: 25px;
  }
  .contact__icon { width: 12px; height: 12px; flex: none; }

  .back-mark {
    position: absolute;
    left: 0; right: 0;
    top: 95px;
    display: flex;
    flex-direction: column;
    align-items: center;
    gap: 22px;
  }
  .back-mark__circle {
    width: 98px; height: 98px;
    border: 3px solid var(--accent);
    border-radius: 50%;
  }
  .back-mark__name {
    font-family: "Open Sans", sans-serif;
    font-weight: 600;
    font-size: 29px;
    color: var(--ink);
    white-space: nowrap;
  }
</style>
</head>
<body>
<main class="stage">

  <section class="card card--front" aria-label="Business card front">
    <svg class="front-band" viewBox="0 0 587 362" width="587" height="362" aria-hidden="true">
      <polygon points="560,0 587,0 587,362 15,362" fill="var(--accent)"/>
    </svg>

    <div class="front-title">Harbourline Recruitment Ltd</div>

    <div class="contact">
      <div class="contact__name">Tom Ashford</div>
      <div class="contact__line">07834 206 148
        <svg class="contact__icon" viewBox="0 0 12 12" aria-hidden="true"><rect x="3" y="0.5" width="6.5" height="11" rx="1.2" fill="none" stroke="#fff" stroke-width="1.2"/><line x1="4.5" y1="9" x2="8" y2="9" stroke="#fff" stroke-width="1"/></svg>
      </div>
      <div class="contact__line">07712 438 560
        <svg class="contact__icon" viewBox="0 0 12 12" aria-hidden="true"><rect x="3" y="0.5" width="6.5" height="11" rx="1.2" fill="none" stroke="#fff" stroke-width="1.2"/><line x1="4.5" y1="9" x2="8" y2="9" stroke="#fff" stroke-width="1"/></svg>
      </div>
      <div class="contact__line">tom.ashford@harbourline-staffing.com
        <svg class="contact__icon" viewBox="0 0 12 12" aria-hidden="true"><rect x="0.5" y="2.5" width="11" height="7.5" fill="#fff"/><polyline points="0.5,2.5 6,7 11.5,2.5" fill="none" stroke="var(--accent)" stroke-width="1"/></svg>
      </div>
      <div class="contact__line">tommashford
        <svg class="contact__icon" viewBox="0 0 12 12" aria-hidden="true"><circle cx="6" cy="6" r="5.5" fill="#fff"/></svg>
      </div>
    </div>
  </section>

  <section class="card card--back" aria-label="Business card back">
    <div class="back-mark">
      <div class="back-mark__circle" aria-hidden="true"></div>
      <div class="back-mark__name">Harbourline Recruitment</div>
    </div>
  </section>

</main>
</body>
</html>
```